Business Card

Can you please copy the format provided for the business cards.
Can the logo be in the colours of the last file as specified.

Can the text please be in grey

• Navy Blue: #00457C
• Grey Text: #555555
• Orange Text: #FDBF29

The names on the business card will be

Dorian Pike
0455 718 302
dorian.pike@tallowridgeleasing.example.au

Lvl 7, 14 Harlow Pde
Merrivale QLD 4388
PO Box 3412
Sunhaven MC QLD 9812
P: 1300 742 619
F: 1300 742 638
www.tallowridgeleasing.example.au

And

Leon Whitcombe
0467 590 148
leon.whitcombe@tallowridgeleasing.example.au

Lvl 7, 14 Harlow Pde
Merrivale QLD 4388
PO Box 3412
Sunhaven MC QLD 9812
P: 1300 742 619
F: 1300 743 905

```html
<!DOCTYPE html>
<html lang="en">
<head>
<meta charset="utf-8">
<title>Tallow Ridge Leasing – Business Cards</title>
<link rel="stylesheet" href="https://fonts.googleapis.com/css2?family=Open+Sans:wght@400;700&display=swap">
<style>
  :root {
    --navy: #00457C;
    --grey-text: #555555;
    --orange: #FDBF29;
    --card: #ffffff;
    --backdrop: #d9dbde;
    --rule: #222222;
  }
  * { box-sizing: border-box; margin: 0; padding: 0; }
  html, body {
    width: 1200px; height: 1000px; overflow: hidden;
    background: var(--backdrop);
    font-family: "Open Sans", Arial, sans-serif;
  }
  .stage {
    width: 1200px; height: 1000px;
    display: flex; flex-direction: column; align-items: center; justify-content: center;
    gap: 44px;
  }
  .card {
    position: relative;
    width: 760px; height: 440px;
    background: var(--card);
    box-shadow: 0 6px 18px rgba(0,0,0,0.18);
    overflow: hidden;
  }
  .brand {
    position: absolute;
    display: flex; align-items: center; gap: 12px;
  }
  .brand-mark {
    width: 34px; height: 34px;
    background: var(--navy);
  }
  .brand-name {
    font-weight: 700;
    font-size: 22px;
    letter-spacing: 0.5px;
    color: var(--navy);
    text-transform: uppercase;
    white-space: nowrap;
  }

  /* Address side */
  .card-back .brand { left: 70px; top: 140px; }
  .divider {
    position: absolute; left: 430px; top: 110px;
    width: 1.5px; height: 220px; background: var(--rule);
  }
  .address {
    position: absolute; left: 458px; top: 150px;
    color: var(--grey-text); font-size: 17px; line-height: 24px;
    list-style: none;
  }
  .website {
    position: absolute; right: 40px; bottom: 40px;
    color: var(--grey-text); font-size: 17px;
  }

  /* Name side */
  .card-front .brand { left: 70px; top: 70px; }
  .contact {
    position: absolute; left: 70px; top: 220px;
    color: var(--grey-text);
  }
  .contact-name { font-size: 28px; line-height: 38px; font-weight: 400; }
  .contact-phone { font-size: 26px; line-height: 36px; }
  .contact-email { font-size: 17px; line-height: 30px; margin-top: 2px; }
  .tagline {
    position: absolute; right: 60px; top: 215px;
    text-align: right; color: var(--grey-text);
    font-size: 26px; line-height: 34px;
  }
  .tagline .accent-orange { color: var(--orange); font-weight: 700; }
  .tagline .accent-navy { color: var(--navy); font-weight: 700; }
</style>
</head>
<body>
<main class="stage">

  <section class="card card-back" aria-label="Business card, address side">
    <div class="brand">
      <span class="brand-mark"></span>
      <span class="brand-name">Tallow Ridge Leasing</span>
    </div>
    <div class="divider"></div>
    <ul class="address">
      <li>Lvl 7, 14 Harlow Pde</li>
      <li>Merrivale QLD 4388</li>
      <li>PO Box 3412</li>
      <li>Sunhaven MC QLD 9812</li>
      <li>P: 1300 742 619</li>
      <li>F: 1300 742 638</li>
    </ul>
    <p class="website">www.tallowridgeleasing.example.au</p>
  </section>

  <section class="card card-front" aria-label="Business card, name side">
    <div class="brand">
      <span class="brand-mark"></span>
      <span class="brand-name">Tallow Ridge Leasing</span>
    </div>
    <div class="contact">
      <p class="contact-name">Dorian Pike</p>
      <p class="contact-phone">0455 718 302</p>
      <p class="contact-email">dorian.pike@tallowridgeleasing.example.au</p>
    </div>
    <p class="tagline">
      Lease it <span class="accent-orange">SMARTER</span><br>
      Grow it <span class="accent-navy">STRONGER</span>
    </p>
  </section>

</main>
</body>
</html>
```